11X17 Poster Drop A Dress Size Challenge

We are having a 21-Day Drop A Dress Size Challenge for our Fitness Studio. We need a poster designed using the template attached as a reference. I have included our Vormaleo Bootcamps logo to put in the poster as well. Please DO NOT use the graphics in the flyer as we are expecting something much better :)
- Size needed 11x17 with bleeding for printing
- We need this made in Photoshop (CS3 friendly) or at least delivered in PS as we might change some text or re-arrange the design later on.

Target Market(s)

Personal Training Studio

Industry/Entity Type

Printing

Colors
0255a3
3377b5
85acd3
f37123
f68e4e
faa54b
f78f20
0692cd
34a7d8

Requirements
Must have
• Must be 11x17 with bleed for printing
• Must be in PS file (CS3 compatible)
• Must include our Vormaleo Bootcamps logo somewhere in the poster
• Must include the information provided in the attached flyer
Nice to have
• Nice to have quality graphics that coincide with the challenge and our logo
Should not have
• Please NO scantily dressed women :)

```html
<!DOCTYPE html>
<html lang="en">
<head>
<meta charset="utf-8">
<title>Drop A Dress Size In 21 Days – Vormaleo Bootcamps</title>
<link rel="stylesheet" href="https://fonts.googleapis.com/css2?family=Bebas+Neue&family=Oswald:wght@400;500;600&display=swap">
<style>
:root{
  --navy:#0255a3;
  --blue:#3377b5;
  --sky:#85acd3;
  --cyan:#0692cd;
  --cyan-light:#34a7d8;
  --orange:#f78f20;
  --orange-deep:#f37123;
  --orange-soft:#f68e4e;
  --gold:#faa54b;
  --white:#ffffff;
}
*{margin:0;padding:0;box-sizing:border-box}
html,body{width:776px;height:1200px;overflow:hidden;background:var(--white)}
.poster{position:relative;width:776px;height:1200px;overflow:hidden;background:var(--cyan-light);font-family:"Oswald",sans-serif}
.backdrop{position:absolute;left:0;top:0}
.drop-ribbon{position:absolute;left:48px;top:24px;width:102px;height:440px}
.drop-word{position:absolute;left:50px;top:44px;width:98px;height:350px;display:flex;align-items:center;justify-content:center}
.drop-word span{display:block;white-space:nowrap;transform:rotate(90deg);font-family:"Bebas Neue",sans-serif;font-size:124px;line-height:90px;letter-spacing:12px;color:var(--gold);text-shadow:-4px 4px 0 var(--navy)}
.headline{position:absolute;left:164px;top:66px;transform:skewY(7deg);transform-origin:left top;font-family:"Bebas Neue",sans-serif;font-weight:400;color:var(--gold);text-shadow:-5px 5px 0 var(--blue);line-height:.82}
.headline .line{display:block;font-size:128px;letter-spacing:-1px}
.headline .line.big{font-size:178px;letter-spacing:-3px}
.prize{position:absolute;right:26px;top:64px;width:250px;text-align:right;font-family:"Bebas Neue",sans-serif;font-size:17px;line-height:1.2;color:var(--navy);letter-spacing:.3px}
.photo{position:absolute;left:500px;top:150px;width:260px;height:570px;background:linear-gradient(180deg,#f3d4b4 0%,#f6a9c3 38%,#f6a9c3 62%,#2f4a73 100%);border-radius:120px 120px 20px 20px;opacity:.95}
.claim{position:absolute;left:236px;top:490px;transform:rotate(12deg);transform-origin:left top}
.claim-label{font-family:"Bebas Neue",sans-serif;font-size:24px;color:var(--navy);letter-spacing:1px;margin-left:34px}
.claim-url{display:inline-block;margin-top:2px;padding:4px 24px 4px 30px;background:var(--orange);font-family:"Bebas Neue",sans-serif;font-size:26px;color:var(--navy);letter-spacing:.5px;clip-path:polygon(14px 0,100% 0,100% 100%,14px 100%,0 50%)}
.start-date{position:absolute;left:22px;top:584px;display:flex;align-items:flex-end;font-family:"Bebas Neue",sans-serif;color:var(--gold);text-shadow:-3px 3px 0 var(--navy)}
.start-date .starts{font-size:32px;writing-mode:vertical-rl;transform:rotate(180deg);line-height:1;margin-right:4px}
.start-date .dates{display:flex;flex-direction:column;line-height:.84}
.start-date .day{font-size:38px}
.start-date .year{font-size:70px}
.urgency{position:absolute;left:0;top:680px;display:flex;align-items:center;height:30px;font-family:"Bebas Neue",sans-serif;font-size:21px;letter-spacing:.5px}
.urgency .hurry{background:var(--sky);color:var(--navy);padding:4px 26px 2px 18px;height:30px;clip-path:polygon(0 0,100% 0,calc(100% - 12px) 100%,0 100%)}
.urgency .call{background:var(--cyan);color:var(--white);padding:4px 40px 2px 26px;height:30px;margin-left:-6px;clip-path:polygon(12px 0,calc(100% - 14px) 0,100% 50%,calc(100% - 14px) 100%,0 100%)}
.details{position:absolute;left:0;top:740px;width:776px;height:460px}
.pitch{position:absolute;left:40px;top:62px;width:240px;font-family:"Bebas Neue",sans-serif;font-size:18px;line-height:1.2;color:var(--white);letter-spacing:.4px}
.pitch p{margin-bottom:24px}
.pitch .lead{color:var(--orange)}
.pitch .close{color:var(--gold);font-size:22px;line-height:1.15}
.offer{position:absolute;left:322px;top:90px;width:430px}
.offer-tag{display:inline-block;background:var(--cyan-light);color:var(--navy);font-family:"Bebas Neue",sans-serif;font-size:23px;padding:6px 34px 2px 14px;text-decoration:underline;text-underline-offset:3px;clip-path:polygon(0 0,calc(100% - 16px) 0,100% 50%,calc(100% - 16px) 100%,0 100%)}
.offer-list{list-style:none;margin-top:22px;padding-left:12px}
.offer-list li{position:relative;padding-left:20px;margin-bottom:12px;font-family:"Bebas Neue",sans-serif;font-size:17px;line-height:1.22;color:var(--blue);letter-spacing:.3px}
.offer-list li::before{content:"";position:absolute;left:0;top:3px;border-left:10px solid var(--cyan);border-top:6px solid transparent;border-bottom:6px solid transparent}
.offer-list strong{font-weight:400;color:var(--navy)}
.brand{position:absolute;left:318px;top:412px;display:flex;align-items:center;gap:5px;font-family:"Bebas Neue",sans-serif;font-size:15px;color:var(--navy);background:var(--white);padding:4px 7px 2px}
.brand .mark{width:9px;height:9px;background:var(--navy)}
.value{position:absolute;left:448px;top:410px;background:var(--cyan-light);color:var(--white);font-family:"Bebas Neue",sans-serif;font-size:16px;padding:5px 40px 3px 22px;clip-path:polygon(12px 0,100% 0,100% 100%,12px 100%,0 50%)}
.price{position:absolute;left:674px;top:368px;width:96px;height:96px;border-radius:50%;background:var(--cyan-light);border:3px solid var(--white);display:flex;flex-direction:column;align-items:center;justify-content:center;transform:rotate(-10deg);font-family:"Bebas Neue",sans-serif;color:var(--white);text-shadow:-2px 2px 0 var(--navy)}
.price small{font-size:15px;color:var(--orange);text-shadow:none}
.price b{font-weight:400;font-size:44px;line-height:.9}
</style>
</head>
<body>
<main class="poster">
  <svg class="backdrop" width="776" height="1200" viewBox="0 0 776 1200" aria-hidden="true">
    <defs>
      <linearGradient id="sky-fill" x1="0" y1="0" x2="1" y2="1">
        <stop offset="0" stop-color="#7fcdf0"/>
        <stop offset="1" stop-color="#34a7d8"/>
      </linearGradient>
    </defs>
    <rect width="776" height="760" fill="url(#sky-fill)"/>
    <polygon points="560,0 776,0 776,170" fill="#85acd3"/>
    <polygon points="150,130 776,200 776,520 150,430" fill="#3377b5" opacity=".55"/>
    <polygon points="280,70 760,24 760,48 292,94" fill="#f78f20"/>
    <line x1="150" y1="94" x2="776" y2="196" stroke="#fff" stroke-width="10" stroke-dasharray="38 22" opacity=".85"/>
    <line x1="150" y1="440" x2="560" y2="528" stroke="#fff" stroke-width="10" stroke-dasharray="38 22" opacity=".85"/>
    <polygon points="0,500 776,640 776,660 0,525" fill="#2b2f36"/>
    <polygon points="0,525 776,660 776,720 0,720" fill="#0255a3"/>
    <polygon points="0,710 776,740 776,790 0,740" fill="#2b2f36"/>
    <polygon points="0,740 776,790 776,812 0,770" fill="#d9dde2"/>
    <rect x="0" y="770" width="776" height="430" fill="#0255a3"/>
    <polygon points="0,770 776,812 776,830 0,790" fill="#d9dde2"/>
    <polygon points="282,795 776,828 776,1200 300,1200" fill="#f78f20"/>
  </svg>

  <svg class="drop-ribbon" viewBox="0 0 102 440" aria-hidden="true">
    <polygon points="0,0 102,0 102,400 51,440 0,400" fill="#3377b5"/>
  </svg>
  <div class="drop-word"><span>DROP</span></div>

  <h1 class="headline">
    <span class="line">A DRESS</span>
    <span class="line">SIZE IN</span>
    <span class="line big">21DAYS</span>
  </h1>

  <p class="prize">Winner gets $100 cash, a new dress<br>( up to $100 value )<br>and a free photo shoot!<br>( $150 value )</p>

  <div class="photo" role="img" aria-label="Photo of a smiling woman in a pink top holding out the waistband of loose jeans"></div>

  <div class="claim">
    <div class="claim-label">Claim your spot now —</div>
    <div class="claim-url">www.vormaleobootcamps.com</div>
  </div>

  <div class="start-date">
    <span class="starts">STARTS</span>
    <span class="dates"><span class="day">APRIL 6TH</span><span class="year">2015</span></span>
  </div>

  <div class="urgency">
    <span class="hurry">Hurry! Space is limited ladies!!</span>
    <span class="call">Call 555-014-2738</span>
  </div>

  <section class="details">
    <div class="pitch">
      <p><span class="lead">Are you tired</span> of all the health clubs and fitness centers that tell you exactly what you want to hear to get you to join, but once you're a member they forget about you and don't teach you anything about how to get results?</p>
      <p><span class="lead">Are you frustrated</span> by all the gimmicks; the pills, powders, shakes and gadgets sold on late night TV that are nothing more than empty promises and slick marketing?</p>
      <p class="close">If so, then this amazing offer is perfect for you…</p>
    </div>

    <div class="offer">
      <span class="offer-tag">Here's what you get:</span>
      <ul class="offer-list">
        <li>Three weeks worth of <strong>fat burning workouts</strong> with a certified personal trainer to make sure that you don't spend one minute exercising that doesn't produce results.</li>
        <li><strong>21 days of fat burning meal plans</strong> designed by a registered dietician to ensure that you reach your goals as quickly as possible.</li>
        <li><strong>Nutrition coaching session</strong> to answer all your questions and set you up for success</li>
        <li><strong>21 days of lessons</strong> to keep you on track to achieving your goal of dropping a dress size</li>
      </ul>
    </div>

    <div class="value">…You get all this – a $327 value</div>
    <div class="brand"><span class="mark"></span>Vormaleo Bootcamps</div>
    <div class="price"><small>For only</small><b>$97!</b></div>
  </section>
</main>
</body>
</html>
```